Driving-coach/trainer who wants to inform about the offer and how I can help people to drive more re

I need a flyer that informs potential customers about my offer.

DL size 210 mm x 99 mm, vertical!

I'm a trainer/coach who helps people to drive a car more relaxed, without fear and more confident.

It's a one to one training. I do train people in their own car. It gets people their freedom back to go where and when they like to go by own car...

Target Market(s)

People (man an woman) who are afraid of driving a car, or are very stressed while driving....

Industry/Entity Type

Life Coaching

Font styles to use
Sans Serif

Colors
acd136

Requirements
Must have
• Page 1:
• -my offer (see text-pdf)
• -three fotos (see attached files "Pixmarra") of people who are satisfied with my offer
• Page 2:
• -advantages in the work with me.
• -contact information
• -and a picture of me (see attached file) next to the contact information or the advantages of my work
• -my logo (see attached file) on Page 1 + 2
• -i like a "clear" and structured layout. "Less is more"

```html
<!DOCTYPE html>
<html lang="de">
<head>
<meta charset="utf-8">
<title>Fahrangst erfolgreich überwinden – Flyer</title>
<link href="https://fonts.googleapis.com/css2?family=Oswald:wght@400;500&family=Source+Sans+3:wght@400;600;700&display=swap" rel="stylesheet">
<style>
  :root{
    --green:#acd136;
    --green-text:#94bf2c;
    --grey-text:#4d4d4d;
    --title-grey:#555;
    --panel:#f1f1f1;
    --page:#e4e4e4;
    --white:#fff;
  }
  *{box-sizing:border-box;margin:0;padding:0}
  html,body{width:1126px;height:1200px;overflow:hidden}
  body{background:var(--page);font-family:"Source Sans 3",Arial,sans-serif;color:var(--grey-text);position:relative}
  .flyer{position:absolute;top:70px;width:500px;height:1060px;background:var(--white);overflow:hidden;box-shadow:0 4px 14px rgba(0,0,0,.25)}
  .flyer--front{left:42px}
  .flyer--back{left:584px}
  .abs{position:absolute}
  .panel{position:absolute;left:0;right:0;background:var(--panel)}
  .headline{position:absolute;top:22px;left:0;right:0;text-align:center;font-size:23px;font-weight:600;color:var(--title-grey);letter-spacing:.2px}
  .headline em{font-style:normal;color:var(--green-text)}
  .condensed{font-family:"Oswald","Arial Narrow",sans-serif;text-transform:uppercase;font-weight:400}
  .badge{position:absolute;left:322px;top:303px;width:140px;height:140px;border-radius:50%;background:var(--green);border:4px solid #fff;box-shadow:0 3px 8px rgba(0,0,0,.3);display:flex;align-items:center;justify-content:center;text-align:center;color:#fff;font-size:18px;line-height:1.3}
  .wollen{top:440px;left:0;right:0;text-align:center;color:var(--green-text);font-size:37px;font-weight:500}
  .questions{top:498px;left:55px;list-style:none;font-size:18px;line-height:28px}
  .questions li{display:flex;align-items:center;gap:14px}
  .dot{width:15px;height:15px;border-radius:50%;background:var(--green);display:inline-flex;align-items:center;justify-content:center}
  .pill{position:absolute;height:34px;border-radius:17px;background:var(--green);color:#fff;display:flex;align-items:center;justify-content:center;font-size:18px;box-shadow:0 2px 4px rgba(0,0,0,.2)}
  .pill--front{left:95px;width:310px;top:601px}
  .pill--back{left:93px;width:310px;top:510px;font-size:19px}
  .situations-title{top:655px;left:0;right:0;text-align:center;color:var(--green-text);font-size:18px}
  .checklist{list-style:none;font-size:12.4px;line-height:14px}
  .checklist li{position:relative;padding-left:18px;margin-bottom:10px;text-align:justify}
  .checklist li svg{position:absolute;left:0;top:2px}
  .checklist .hl{color:var(--green-text)}
  .checklist--front{top:685px;left:20px;width:456px}
  .checklist--back{top:568px;left:22px;width:450px}
  .checklist--back li{margin-bottom:6px}
  .slogan{left:300px;width:170px;top:905px;text-align:center;color:var(--green-text);font-size:23px;line-height:26px}
  .contact{position:absolute;left:20px}
  .contact .phone{display:flex;align-items:center;gap:8px;font-size:18px;font-weight:700;color:var(--green-text)}
  .contact .web{font-size:15px;font-weight:700;color:var(--green-text);margin-top:2px}
  .steps-title{top:362px;left:0;right:0;text-align:center;color:var(--green-text);font-size:20px}
  .step{position:absolute;top:393px;width:104px;height:104px;border-radius:50%;background:var(--green);border:3px solid #fff;box-shadow:0 0 0 1px #d6d6d6;color:#fff;text-align:center;display:flex;flex-direction:column;align-items:center;padding-top:8px}
  .step .num{font-family:"Oswald",sans-serif;font-size:30px;line-height:38px}
  .step .txt{font-size:10.5px;line-height:11px;padding:0 8px}
  .quote{top:790px;left:22px;font-size:15px;line-height:19px;color:#333}
  .quote .mark{color:var(--green);font-size:28px;font-family:Georgia,serif;line-height:0}
  .coach-name{top:855px;left:20px;color:var(--green-text);font-size:19px;letter-spacing:2px}
  .coach-role{top:878px;left:20px;color:var(--green-text);font-size:15px;letter-spacing:1.5px}
</style>
</head>
<body>

<!-- Front side -->
<section class="flyer flyer--front">
  <div class="panel" style="top:300px;height:640px"></div>
  <h1 class="headline">FAHRANGST <em>ERFOLGREICH</em> ÜBERWINDEN!</h1>

  <svg class="abs" style="top:60px;left:0" width="500" height="360" viewBox="0 0 500 360">
    <defs>
      <linearGradient id="frontPhoto" x1="0" y1="0" x2="1" y2="1">
        <stop offset="0" stop-color="#8a8378"/>
        <stop offset=".5" stop-color="#c49a6c"/>
        <stop offset="1" stop-color="#5d5a55"/>
      </linearGradient>
    </defs>
    <path d="M0,26 Q250,-14 500,40 L500,58 Q250,8 0,46 Z" fill="var(--green)"/>
    <path d="M0,46 Q250,8 500,58 L500,290 Q300,250 0,300 Z" fill="url(#frontPhoto)" role="img" aria-label="Photo: smiling woman driving a convertible"/>
    <path d="M0,300 Q300,250 500,290 L500,300 Q280,300 0,360 Z" fill="var(--green)"/>
  </svg>

  <div class="badge condensed" style="font-family:'Source Sans 3',sans-serif">ICH HAB’S<br>GESCHAFFT!!</div>

  <h2 class="abs condensed wollen">Wollen Sie</h2>
  <ul class="abs questions">
    <li><span class="dot"><svg width="9" height="9" viewBox="0 0 10 10"><path d="M1.5,5 L4,7.5 L8.5,2.5" stroke="#fff" stroke-width="1.8" fill="none"/></svg></span>Fahrangst überwinden?</li>
    <li><span class="dot"><svg width="9" height="9" viewBox="0 0 10 10"><path d="M1.5,5 L4,7.5 L8.5,2.5" stroke="#fff" stroke-width="1.8" fill="none"/></svg></span>Panikattacken beim Auto fahren loswerden?</li>
    <li><span class="dot"><svg width="9" height="9" viewBox="0 0 10 10"><path d="M1.5,5 L4,7.5 L8.5,2.5" stroke="#fff" stroke-width="1.8" fill="none"/></svg></span>Sicher und entspannt Autofahren?</li>
  </ul>

  <div class="pill pill--front condensed">Dann sind Sie hier richtig!</div>

  <h3 class="abs condensed situations-title">Kommt Ihnen eine dieser Situationen bekannt vor?</h3>
  <ul class="abs checklist checklist--front">
    <li><svg width="11" height="9" viewBox="0 0 11 9"><path d="M1,4.5 L4,7.5 L10,1" stroke="var(--green)" stroke-width="2" fill="none"/></svg><span class="hl">Autofahren erleben Sie unter hoher Anspannung und Stress.</span> - Sie wünschen sich, Autofahren sicher und entspannt zu erleben.</li>
    <li><svg width="11" height="9" viewBox="0 0 11 9"><path d="M1,4.5 L4,7.5 L10,1" stroke="var(--green)" stroke-width="2" fill="none"/></svg><span class="hl">Bestimmte Situationen (z.B. unbekannte Strecken, Autobahnen, Baustellen, Stadtverkehr, Fahrspurwechsel, Einparken...) bereiten Ihnen großen Stress, und Sie trauen sie sich nicht (mehr) zu.</span> - Sie möchten diese Situationen gelassen und souverän meistern.</li>
    <li><svg width="11" height="9" viewBox="0 0 11 9"><path d="M1,4.5 L4,7.5 L10,1" stroke="var(--green)" stroke-width="2" fill="none"/></svg><span class="hl">Sie fühlen sich durch andere Verkehrsteilnehmer gestresst und unter Druck gesetzt. Sie haben Angst, auf unvorhergesehene Situationen nicht richtig zu reagieren.</span> - Sie möchten Autofahren entspannter und souveräner erleben.</li>
    <li><svg width="11" height="9" viewBox="0 0 11 9"><path d="M1,4.5 L4,7.5 L10,1" stroke="var(--green)" stroke-width="2" fill="none"/></svg><span class="hl">Angst oder Panikattacken begleiten Sie beim Autofahren. Vielleicht vermeiden Sie deshalb das Autofahren komplett.</span> - Sie möchten/müssen (beruflich) mobil sein und bleiben.</li>
  </ul>

  <svg class="abs" style="top:920px;left:0" width="500" height="140" viewBox="0 0 500 140">
    <path d="M0,30 Q90,-5 200,30 Q330,80 420,70 Q470,62 500,40 L500,140 L0,140 Z" fill="var(--white)"/>
    <path d="M0,22 Q90,-10 200,24 Q120,0 0,30 Z" fill="var(--green)"/>
    <path d="M320,100 Q440,100 500,40 L500,60 Q440,115 320,100 Z" fill="var(--green)"/>
  </svg>

  <div class="abs condensed slogan">Auch Sie<br>können<br>es schaffen!!</div>

  <div class="contact" style="top:990px">
    <div class="phone"><svg width="16" height="16" viewBox="0 0 24 24"><path d="M6.6,10.8c1.4,2.8,3.8,5.1,6.6,6.6l2.2-2.2c.3-.3.7-.4,1-.2 1.1.4,2.3.6,3.6.6.6,0,1,.4,1,1V20c0,.6-.4,1-1,1C10.6,21,3,13.4,3,4c0-.6.4-1,1-1h3.5c.6,0,1,.4,1,1 0,1.3.2,2.5.6,3.6.1.3,0,.7-.2,1Z" fill="var(--green-text)"/></svg>0155 01 23 45 67</div>
    <div class="web">www.ruhig-am-steuer.de</div>
  </div>
</section>

<!-- Back side -->
<section class="flyer flyer--back">
  <div class="panel" style="top:280px;height:680px"></div>
  <h1 class="headline">FAHRANGST <em>ERFOLGREICH</em> ÜBERWINDEN!</h1>

  <svg class="abs" style="top:60px;left:0" width="500" height="300" viewBox="0 0 500 300">
    <defs>
      <linearGradient id="backPhoto" x1="0" y1="0" x2="1" y2="0">
        <stop offset="0" stop-color="#9aa07a"/>
        <stop offset=".5" stop-color="#d8b48c"/>
        <stop offset="1" stop-color="#6f747a"/>
      </linearGradient>
    </defs>
    <path d="M0,28 Q250,-12 500,42 L500,58 Q250,6 0,44 Z" fill="var(--green)"/>
    <path d="M0,44 Q250,6 500,58 L500,210 Q320,170 0,230 Z" fill="url(#backPhoto)" role="img" aria-label="Photo: happy young woman at a car window giving a thumbs up"/>
    <path d="M0,220 Q320,160 500,210 L500,222 Q300,200 0,280 Z" fill="var(--green)"/>
  </svg>

  <h2 class="abs condensed steps-title">3 Schritte zur Lösung:</h2>
  <div class="step" style="left:62px"><span class="num">1.</span><span class="txt">Erstgespräch vereinbaren</span></div>
  <div class="step" style="left:198px"><span class="num">2.</span><span class="txt" style="font-size:9px;line-height:10px">Analyse Ihrer individuellen Situation und Zielsetzung</span></div>
  <div class="step" style="left:332px"><span class="num">3.</span><span class="txt">Individuelles Coaching und Training</span></div>

  <div class="pill pill--back condensed">Ihre Vorteile in der Arbeit mit mir:</div>

  <ul class="abs checklist checklist--back">
    <li><svg width="11" height="9" viewBox="0 0 11 9"><path d="M1,4.5 L4,7.5 L10,1" stroke="var(--green)" stroke-width="2" fill="none"/></svg><span class="hl">Über 10 Jahre Erfahrung als Fahrsicherheits-Trainerin und Fahrangst-Bewältigung-Coach:</span> Ich helfe Ihnen gezielt, Entspannungstechniken einzusetzen und Ängste und Panik beim Autofahren zu überwinden. Sie profitieren von meinen Tipps &amp; Tricks bei Unsicherheiten z.B. beim Fahrspurwechsel, Einparken, Autobahn...</li>
    <li><svg width="11" height="9" viewBox="0 0 11 9"><path d="M1,4.5 L4,7.5 L10,1" stroke="var(--green)" stroke-width="2" fill="none"/></svg><span class="hl">100 % auf Sie zugeschnitten:</span> Ich begleite Sie zielführend in Ihrem individuellen Prozess der Angst-/Paniküberwindung und/oder Erhöhung Ihrer Fahrsicherheit/-kompetenz.</li>
    <li><svg width="11" height="9" viewBox="0 0 11 9"><path d="M1,4.5 L4,7.5 L10,1" stroke="var(--green)" stroke-width="2" fill="none"/></svg>Wir <span class="hl">trainieren Schritt für Schritt -exakt auf Sie abgestimmt!- in Ihrem eigenen Fahrzeug</span></li>
    <li><svg width="11" height="9" viewBox="0 0 11 9"><path d="M1,4.5 L4,7.5 L10,1" stroke="var(--green)" stroke-width="2" fill="none"/></svg>Wenn es Ihnen nicht möglich ist, in meine Praxis zu kommen:<br><span class="hl">Mit der „mobilen Praxis“ komme ich auch zu Ihnen.</span></li>
  </ul>

  <svg class="abs" style="top:760px;left:290px" width="190" height="300" viewBox="0 0 190 300" role="img" aria-label="Portrait photo of the coach in a white blouse">
    <defs>
      <linearGradient id="portrait" x1="0" y1="0" x2="0" y2="1">
        <stop offset="0" stop-color="#b59a86"/>
        <stop offset=".45" stop-color="#ededed"/>
        <stop offset="1" stop-color="#ffffff"/>
      </linearGradient>
    </defs>
    <path d="M60,20 Q95,-10 130,20 L140,120 Q185,140 190,240 L190,300 L0,300 L10,200 Q20,140 55,120 Z" fill="url(#portrait)"/>
  </svg>

  <p class="abs quote"><span class="mark">“</span> Auch Sie können es schaffen!<br>&nbsp;&nbsp;&nbsp;Ich helfe Ihnen dabei. <span class="mark">”</span></p>
  <div class="abs coach-name">Katrin Lindqvist</div>
  <div class="abs coach-role">Fahrangst-Bewältigungs-Coach</div>

  <svg class="abs" style="top:900px;left:0" width="500" height="160" viewBox="0 0 500 160">
    <path d="M0,20 Q80,-5 180,25 Q320,80 380,110 Q450,130 500,60 L500,160 L0,160 Z" fill="var(--white)"/>
    <path d="M0,14 Q80,-10 180,18 Q90,2 0,24 Z" fill="var(--green)"/>
    <path d="M300,130 Q440,150 500,80 L500,100 Q430,165 300,130 Z" fill="var(--green)"/>
  </svg>

  <div class="contact" style="top:992px">
    <div class="phone"><svg width="16" height="16" viewBox="0 0 24 24"><path d="M6.6,10.8c1.4,2.8,3.8,5.1,6.6,6.6l2.2-2.2c.3-.3.7-.4,1-.2 1.1.4,2.3.6,3.6.6.6,0,1,.4,1,1V20c0,.6-.4,1-1,1C10.6,21,3,13.4,3,4c0-.6.4-1,1-1h3.5c.6,0,1,.4,1,1 0,1.3.2,2.5.6,3.6.1.3,0,.7-.2,1Z" fill="var(--green-text)"/></svg>0155 01 23 45 67</div>
    <div class="web">www.ruhig-am-steuer.de</div>
  </div>
</section>

</body>
</html>
```